Stationery Design
Business Card, Envelopes and letterhead
Professional
Dwight Halloway
Production Manager
4172 N. Wrenfield Rd.
Baton Rouge LA 70913
dwight@velmorpack.com
www.velmorpack.com
Please propose letterhead, business card and envelope design using the new logo just uploaded

```html
<!DOCTYPE html>
<html lang="en">
<head>
<meta charset="utf-8">
<title>Velmor Pack Stationery</title>
<link rel="stylesheet" href="https://fonts.googleapis.com/css2?family=Roboto:wght@400;700;900&display=swap">
<style>
  :root {
    --backdrop: #c4c6c8;
    --paper: #ffffff;
    --ink: #2a2d30;
    --ink-soft: #6b6f73;
    --accent: #1fb1e6;
    --flap-line: #d4d6d8;
    --faint-mark: #d9dbdd;
  }
  * { margin: 0; padding: 0; box-sizing: border-box; }
  html, body { width: 1200px; height: 655px; overflow: hidden; }
  body {
    background: var(--backdrop);
    font-family: "Roboto", Arial, sans-serif;
    color: var(--ink);
    position: relative;
  }
  .sheet {
    position: absolute;
    background: var(--paper);
    box-shadow: 0 1px 3px rgba(0,0,0,0.18);
  }

  /* brand lockup */
  .brand { position: absolute; display: flex; flex-direction: column; align-items: flex-start; }
  .brand-row { display: flex; align-items: center; gap: 4px; }
  .brand-dot { border-radius: 50%; background: var(--accent); }
  .brand-name { font-weight: 900; color: var(--ink); letter-spacing: 0.02em; line-height: 1; }
  .brand-tag { font-weight: 700; color: var(--ink); letter-spacing: 0.06em; white-space: nowrap; margin-top: 2px; }

  .web-bar {
    position: absolute;
    background: var(--accent);
    color: #fff;
    font-weight: 700;
    display: flex; align-items: center; justify-content: flex-end;
    padding-right: 4px;
    white-space: nowrap;
  }

  .contact { position: absolute; font-size: 5px; line-height: 1.45; color: var(--ink); }
  .contact .row { display: flex; }
  .contact .label { width: 22px; }
  .contact .gap { height: 4px; }

  /* letterhead */
  .letterhead { left: 187px; top: 12px; width: 432px; height: 631px; }
  .letterhead .brand { left: 29px; top: 24px; }
  .letterhead .brand-dot { width: 14px; height: 14px; }
  .letterhead .brand-name { font-size: 24px; }
  .letterhead .brand-tag { font-size: 4.5px; }
  .letterhead .web-bar { right: 0; top: 26px; width: 62px; height: 12px; font-size: 5.5px; }
  .letterhead .contact { left: 29px; top: 548px; }

  /* business card */
  .card { left: 29px; top: 276px; width: 235px; height: 120px; }
  .card .brand { left: 12px; top: 8px; }
  .card .brand-dot { width: 8px; height: 8px; }
  .card .brand-name { font-size: 14px; }
  .card .brand-tag { font-size: 3px; }
  .card .holder { position: absolute; right: 10px; top: 9px; text-align: right; font-size: 5px; line-height: 1.4; color: var(--accent); font-weight: 700; }
  .card .contact { left: 12px; top: 70px; font-size: 4px; }
  .card .contact .label { width: 17px; }
  .card .contact .gap { height: 2px; }
  .card .web-bar { right: 0; bottom: 12px; width: 72px; height: 7px; font-size: 4px; }

  /* envelope back */
  .envelope-back { left: 660px; top: 108px; width: 499px; height: 199px; }
  .envelope-back svg.flap { position: absolute; inset: 0; }
  .envelope-back .faint-mark {
    position: absolute; left: 50%; top: 58px; transform: translateX(-50%);
    display: flex; flex-direction: column; align-items: center;
  }
  .envelope-back .faint-mark .brand-name { font-size: 30px; color: var(--faint-mark); }
  .envelope-back .faint-mark .brand-tag { font-size: 5px; color: var(--faint-mark); }

  /* envelope front */
  .envelope-front { left: 660px; top: 336px; width: 499px; height: 252px; }
  .envelope-front .brand { left: 18px; top: 22px; }
  .envelope-front .brand-dot { width: 14px; height: 14px; }
  .envelope-front .brand-name { font-size: 26px; }
  .envelope-front .brand-tag { font-size: 4.5px; }
  .envelope-front .web-bar { right: 0; top: 31px; width: 110px; height: 13px; font-size: 6.5px; }
  .envelope-front .contact { left: 19px; top: 150px; }
</style>
</head>
<body>

  <section class="sheet letterhead" aria-label="Letterhead">
    <div class="brand">
      <div class="brand-row"><span class="brand-dot"></span><span class="brand-name">VPK</span></div>
      <span class="brand-tag">VELMOR PACKAGING GROUP</span>
    </div>
    <div class="web-bar">www.velmorpack.com</div>
    <div class="contact">
      <div class="row"><span class="label">Toll free</span><span>1 800 555 0142</span></div>
      <div class="row"><span class="label">Phone</span><span>225 555 0118</span></div>
      <div class="row"><span class="label">Fax</span><span>225 555 0119</span></div>
      <div class="row"><span class="label">Cell</span><span>225 555 0176</span></div>
      <div class="gap"></div>
      <div>dwight@velmorpack.com</div>
      <div>4172 N. Wrenfield Rd. Baton Rouge LA 70913</div>
    </div>
  </section>

  <section class="sheet card" aria-label="Business card">
    <div class="brand">
      <div class="brand-row"><span class="brand-dot"></span><span class="brand-name">VPK</span></div>
      <span class="brand-tag">VELMOR PACKAGING GROUP</span>
    </div>
    <div class="holder">
      <div>Dwight Halloway</div>
      <div>Production Manager</div>
    </div>
    <div class="contact">
      <div class="row"><span class="label">Toll free</span><span>1 800 555 0142</span></div>
      <div class="row"><span class="label">Phone</span><span>225 555 0118</span></div>
      <div class="row"><span class="label">Fax</span><span>225 555 0119</span></div>
      <div class="row"><span class="label">Cell</span><span>225 555 0176</span></div>
      <div class="gap"></div>
      <div>dwight@velmorpack.com</div>
      <div>4172 N. Wrenfield Rd. Baton Rouge LA 70913</div>
    </div>
    <div class="web-bar">www.velmorpack.com</div>
  </section>

  <section class="sheet envelope-back" aria-label="Envelope back">
    <svg class="flap" width="499" height="199" viewBox="0 0 499 199">
      <path d="M0 0 L200 112 Q249.5 136 299 112 L499 0" fill="none" stroke="var(--flap-line)" stroke-width="1.2"/>
    </svg>
    <div class="faint-mark">
      <span class="brand-name">VPK</span>
      <span class="brand-tag">VELMOR PACKAGING GROUP</span>
    </div>
  </section>

  <section class="sheet envelope-front" aria-label="Envelope front">
    <div class="brand">
      <div class="brand-row"><span class="brand-dot"></span><span class="brand-name">VPK</span></div>
      <span class="brand-tag">VELMOR PACKAGING GROUP</span>
    </div>
    <div class="web-bar">www.velmorpack.com</div>
    <div class="contact">
      <div class="row"><span class="label">Toll free</span><span>1 800 555 0142</span></div>
      <div class="row"><span class="label">Phone</span><span>225 555 0118</span></div>
      <div class="row"><span class="label">Fax</span><span>225 555 0119</span></div>
      <div class="row"><span class="label">Cell</span><span>225 555 0176</span></div>
      <div class="gap"></div>
      <div>dwight@velmorpack.com</div>
      <div>4172 N. Wrenfield Rd. Baton Rouge LA 70913</div>
    </div>
  </section>

</body>
</html>
```